Dorian Name Card Design

I would like to have a name card with these information:
Name on Card: Dorian Pelzeck
Job: General Director
Company: BRULENTIX., JSC (BRULENTIX HEAVY EQUIPMENT FABRICATION JOINT STOCK COMPANY)
Address: 7318 Quillfern Dr. ,San Antonio, Texas, US
Tel: 2105497260
Email: DorianPelzeck@brulentix.example
Job: General Director
Tel: 2105497260

Industry/Entity Type

Construction

Requirements
Must have
• Name on Card: Dorian Pelzeck
• Job: General Director
• Company: BRULENTIX., JSC (BRULENTIX HEAVY EQUIPMENT FABRICATION JOINT STOCK COMPANY)
• Address: 7318 Quillfern Dr. ,San Antonio, Texas, US
• Tel: 2105497260
• Email: DorianPelzeck@brulentix.example
Nice to have
• Job: General Director
• Tel: 2105497260
Should not have
• Logo

```html
<!DOCTYPE html>
<html lang="en">
<head>
<meta charset="utf-8">
<title>Dorian Pelzeck – Name Card</title>
<link rel="stylesheet" href="https://fonts.googleapis.com/css2?family=Gentium+Book+Plus:wght@400;700&family=Cinzel:wght@400;500&family=Montserrat:wght@400;500&display=swap">
<style>
  :root {
    --page: #ffffff;
    --frame: #0c0d0d;
    --card: #1e2021;
    --card-edge: #2b2e30;
    --sky: #58b4f2;
    --navy: #0f1d52;
    --royal: #2166cc;
    --white: #ffffff;
    --icon-top: #6db8f6;
    --icon-bottom: #1f5fd0;
  }
  * { box-sizing: border-box; margin: 0; padding: 0; }
  html, body { width: 1200px; height: 702px; overflow: hidden; background: var(--page); }
  .canvas { position: relative; width: 1200px; height: 702px; }

  .card-frame { position: absolute; left: 30px; top: 28px; width: 1141px; height: 646px; background: var(--frame); }
  .card { position: absolute; left: 59px; top: 55px; width: 1086px; height: 591px; background: var(--card); border: 1px solid var(--card-edge); overflow: hidden; }

  .decor { position: absolute; left: 0; top: 0; width: 1200px; height: 702px; }

  .name-band { position: absolute; left: 415px; top: 207px; width: 730px; height: 104px; background: var(--white); box-shadow: 0 6px 12px rgba(0,0,0,.45); }

  .right { position: absolute; right: 147px; text-align: right; white-space: nowrap; }

  .person-name { top: 208px; font-family: "Gentium Book Plus", serif; font-weight: 700; font-size: 52px; letter-spacing: 3px; color: var(--navy); line-height: 1; }
  .person-title { top: 266px; font-family: "Gentium Book Plus", serif; font-weight: 700; font-size: 35px; letter-spacing: 1.5px; color: var(--royal); line-height: 1; }

  .company-name { top: 339px; font-family: "Gentium Book Plus", serif; font-size: 35px; letter-spacing: 2px; color: var(--sky); line-height: 1; }
  .company-full { top: 393px; font-family: "Cinzel", serif; font-weight: 500; font-size: 18px; letter-spacing: .6px; color: var(--white); line-height: 1; }
  .company-full .initial { color: var(--sky); }

  .divider { position: absolute; left: 59px; top: 429px; width: 1086px; height: 3px; background: var(--white); }

  .contact { position: absolute; right: 200px; font-family: "Montserrat", sans-serif; color: var(--white); white-space: nowrap; line-height: 1; }
  .contact-address { top: 466px; font-size: 20px; font-variant: small-caps; font-weight: 500; letter-spacing: 1px; }
  .contact-phone { top: 513px; font-size: 18px; letter-spacing: 1px; }
  .contact-email { top: 563px; font-size: 17px; letter-spacing: .5px; }

  .contact-icon { position: absolute; left: 1013px; width: 40px; height: 40px; }
  .icon-address { top: 453px; }
  .icon-phone { top: 502px; }
  .icon-email { top: 552px; }

  .rule { position: absolute; left: 59px; height: 4px; }
  .rule-short { top: 581px; width: 289px; background: var(--sky); }
  .rule-long { top: 602px; width: 576px; background: var(--white); }
  .rule-mid { top: 621px; width: 362px; background: var(--sky); }
</style>
</head>
<body>
<div class="canvas">
  <div class="card-frame"></div>
  <div class="card"></div>

  <div class="name-band"></div>

  <svg class="decor" viewBox="0 0 1200 702" aria-hidden="true">
    <defs>
      <filter id="socket-shadow" x="-50%" y="-50%" width="200%" height="200%">
        <feDropShadow dx="2" dy="3" stdDeviation="4" flood-color="#000" flood-opacity=".6"/>
      </filter>
    </defs>
    <line x1="309" y1="55" x2="309" y2="140" stroke="var(--sky)" stroke-width="4"/>
    <circle cx="309" cy="144" r="12" fill="var(--sky)"/>
    <line x1="415" y1="55" x2="415" y2="112" stroke="var(--sky)" stroke-width="3"/>
    <circle cx="415" cy="116" r="8" fill="var(--sky)"/>
    <circle cx="382" cy="259" r="52" fill="var(--card)" filter="url(#socket-shadow)"/>
    <line x1="377" y1="55" x2="377" y2="240" stroke="var(--sky)" stroke-width="12"/>
    <circle cx="377" cy="257" r="30" fill="var(--sky)"/>
  </svg>

  <div class="right person-name">Dorian Pelzeck</div>
  <div class="right person-title">General Director</div>

  <div class="right company-name">BRULENTIX, JSC</div>
  <div class="right company-full">(<span class="initial">B</span>RULENTIX <span class="initial">H</span>EAVY <span class="initial">E</span>QUIPMENT <span class="initial">F</span>ABRICATION <span class="initial">J</span>OINT <span class="initial">S</span>TOCK <span class="initial">C</span>OMPANY)</div>

  <div class="divider"></div>

  <div class="contact contact-address">7318 Quillfern Dr. ,San Antonio, Texas, US</div>
  <div class="contact contact-phone">2105497260</div>
  <div class="contact contact-email">DorianPelzeck@brulentix.example</div>

  <svg class="contact-icon icon-address" viewBox="0 0 40 40" aria-hidden="true">
    <defs><linearGradient id="icon-fill" x1="0" y1="0" x2="0" y2="1"><stop offset="0" stop-color="var(--icon-top)"/><stop offset="1" stop-color="var(--icon-bottom)"/></linearGradient></defs>
    <circle cx="20" cy="20" r="18.5" fill="url(#icon-fill)" stroke="var(--white)" stroke-width="2"/>
    <path d="M20 29c-4-5-6.5-8.5-6.5-11.5a6.5 6.5 0 0 1 13 0C26.5 20.5 24 24 20 29z" fill="var(--white)"/>
    <circle cx="20" cy="17.5" r="2.5" fill="var(--icon-bottom)"/>
  </svg>
  <svg class="contact-icon icon-phone" viewBox="0 0 40 40" aria-hidden="true">
    <circle cx="20" cy="20" r="18.5" fill="url(#icon-fill)" stroke="var(--white)" stroke-width="2"/>
    <circle cx="20" cy="20" r="11" fill="none" stroke="var(--white)" stroke-width="1.6"/>
    <path d="M16 13.5l2.2 3.2-1.4 1.5c.8 1.9 2.1 3.3 4 4.3l1.5-1.4 3.2 2.2-1.3 2.5c-4.8-.4-9.5-5.3-9.8-10z" fill="var(--white)"/>
  </svg>
  <svg class="contact-icon icon-email" viewBox="0 0 40 40" aria-hidden="true">
    <circle cx="20" cy="20" r="18.5" fill="url(#icon-fill)" stroke="var(--white)" stroke-width="2"/>
    <path d="M10 19l19-7-5 17-4-6z" fill="var(--white)"/>
    <path d="M20 23l9-11" stroke="var(--icon-bottom)" stroke-width="1.2"/>
  </svg>

  <div class="rule rule-short"></div>
  <div class="rule rule-long"></div>
  <div class="rule rule-mid"></div>
</div>
</body>
</html>
```